Business cards and Stationery for a photograhy studio
Marigold Image Loft
Owen Pryce
Unit 4, 6/F, Harbourline Centre, 28 Fenwick Lane, Kestrel Bay
info@marigoldloft.com.hk
www.marigoldloft.com.hk
please see attachment. Attached are the logo and the envelope die cut (Just for you to know the styles) for your ref. I would like to also have letterhead, envelope, document envelope, paper folder and CD designs
A Chinese version with Chinese company name

```html
<!DOCTYPE html>
<html lang="en">
<head>
<meta charset="utf-8">
<title>Marigold Image Loft — Stationery Set</title>
<link href="https://fonts.googleapis.com/css2?family=Quicksand:wght@400&family=Roboto:wght@400;700&family=Noto+Sans+TC:wght@400&display=swap" rel="stylesheet">
<style>
  :root {
    --stage: #4a4a4a;
    --ink: #050505;
    --paper: #ffffff;
    --brand-red: #ee1c25;
    --muted: #2a2a2a;
    --grey-text: #333333;
  }
  html, body {
    margin: 0;
    padding: 0;
    width: 1200px;
    height: 776px;
    overflow: hidden;
    background: var(--stage);
  }
  .stationery-sheet { display: block; width: 1200px; height: 776px; }
  .brand-name { font-family: "Quicksand", sans-serif; font-weight: 400; fill: var(--brand-red); }
  .brand-name.on-red { fill: var(--paper); }
  .brand-cn { font-family: "Noto Sans TC", sans-serif; font-weight: 400; fill: var(--brand-red); }
  .brand-cn.on-red { fill: var(--paper); }
  .brand-square { fill: none; stroke: var(--brand-red); }
  .brand-square.on-red { stroke: var(--paper); }
  .contact { font-family: "Roboto", sans-serif; font-size: 3.1px; fill: var(--paper); }
  .contact.dark { fill: var(--grey-text); }
  .holder-name { font-family: "Roboto", sans-serif; font-weight: 700; font-size: 3.4px; fill: var(--brand-red); }
  .holder-name .surname { fill: var(--paper); font-weight: 400; }
  .icon { fill: var(--brand-red); }
  .frame-line { fill: none; stroke: var(--brand-red); stroke-width: 0.8; }
  .frame-line.light { stroke: var(--paper); }
  .ink { fill: var(--ink); }
  .paper { fill: var(--paper); }
  .red { fill: var(--brand-red); }
  .cd-label { font-family: "Roboto", sans-serif; fill: var(--muted); text-anchor: middle; }
  .cd-label.client { fill: var(--brand-red); font-weight: 700; }
  .cd-ring-text { font-family: "Roboto", sans-serif; font-size: 4px; fill: #8a8a8a; letter-spacing: 0.3px; }
</style>
</head>
<body>
<svg class="stationery-sheet" viewBox="0 0 1200 776" xmlns="http://www.w3.org/2000/svg" role="img" aria-label="Marigold Image Loft stationery set: business cards, letterheads, envelopes, folder and CD">
  <defs>
    <radialGradient id="glow" cx="0.7" cy="0.15" r="0.6">
      <stop offset="0" stop-color="#2a2a2a"/>
      <stop offset="1" stop-color="#050505"/>
    </radialGradient>
    <path id="cd-ring" d="M890,622 m-104,0 a104,104 0 1,1 208,0 a104,104 0 1,1 -208,0"/>
  </defs>

  <!-- ===== Business card: front with contact ===== -->
  <g class="business-card card-front">
    <rect class="ink" x="65" y="36" width="124" height="71"/>
    <rect class="frame-line" x="68.5" y="39.5" width="117" height="64"/>
    <rect class="brand-square" x="79" y="51" width="9" height="9" stroke-width="0.9"/>
    <text class="brand-name" x="91" y="59.5" font-size="7.2">Marigold Image Loft</text>
    <text class="holder-name" x="80" y="80">OWEN <tspan class="surname">PRYCE</tspan><tspan class="contact" dx="1.5"> |  Photographer</tspan></text>
    <line x1="80" y1="82" x2="174" y2="82" stroke="#555" stroke-width="0.3"/>
    <text class="contact" x="80" y="87">Unit 4, 6/F, Harbourline</text>
    <text class="contact" x="80" y="90.5">Centre, 28 Fenwick Lane,</text>
    <text class="contact" x="80" y="94">Kestrel Bay</text>
    <rect class="icon" x="113" y="84.7" width="2" height="2"/>
    <text class="contact" x="116" y="87">(852) 2310 4478</text>
    <rect class="icon" x="113" y="89.2" width="2" height="2"/>
    <text class="contact" x="116" y="91.5">(852) 9120 3386</text>
    <rect class="icon" x="139" y="84.7" width="2" height="2"/>
    <text class="contact" x="142" y="87">(852) 2310 4479</text>
    <rect class="icon" x="139" y="89.2" width="2" height="2"/>
    <text class="contact" x="142" y="91.5">info@marigoldloft.com.hk</text>
  </g>

  <!-- ===== Business card: back, black ===== -->
  <g class="business-card card-back-black">
    <rect class="ink" x="65" y="111" width="124" height="69"/>
    <rect class="frame-line" x="68.5" y="114.5" width="117" height="62"/>
    <rect class="brand-square" x="97" y="128" width="8" height="8" stroke-width="0.9"/>
    <text class="brand-name" x="107.5" y="135.5" font-size="6.6">Marigold Image Loft</text>
    <text class="brand-cn" x="127" y="159" font-size="6.4" text-anchor="middle">金盞影像工作室</text>
    <circle class="icon" cx="107" cy="171" r="1.1"/>
    <text class="contact" x="109.5" y="172.1">www.marigoldloft.com.hk</text>
  </g>

  <!-- ===== Business card: back, red ===== -->
  <g class="business-card card-back-red">
    <rect class="red" x="65" y="186" width="124" height="71"/>
    <rect class="frame-line light" x="68.5" y="189.5" width="117" height="64"/>
    <rect class="brand-square on-red" x="97" y="201" width="8" height="8" stroke-width="0.9"/>
    <text class="brand-name on-red" x="107.5" y="208.5" font-size="6.6">Marigold Image Loft</text>
    <text class="brand-cn on-red" x="127" y="232" font-size="6.4" text-anchor="middle">金盞影像工作室</text>
    <circle fill="#fff" cx="107" cy="244.5" r="1.1"/>
    <text class="contact" x="109.5" y="245.6">www.marigoldloft.com.hk</text>
  </g>

  <!-- ===== Letterhead ===== -->
  <g class="letterhead">
    <rect class="paper" x="196" y="35" width="219" height="284"/>
    <rect class="ink" x="196" y="35" width="219" height="31"/>
    <rect class="frame-line" x="200.5" y="39.5" width="211" height="275"/>
    <rect class="brand-square" x="214" y="47" width="9" height="9" stroke-width="0.9"/>
    <text class="brand-name" x="226" y="55.5" font-size="7.2">Marigold Image Loft</text>
    <text class="contact" x="306" y="47.5">Unit 4, 6/F, Harbourline Centre, 28 Fenwick Lane, Kestrel Bay</text>
    <rect class="icon" x="306" y="51" width="2" height="2"/>
    <text class="contact" x="309.5" y="53.2">(852) 2310 4478</text>
    <rect class="icon" x="306" y="56.5" width="2" height="2"/>
    <text class="contact" x="309.5" y="58.7">(852) 2310 4479</text>
    <line x1="337" y1="50" x2="337" y2="60" stroke="#666" stroke-width="0.3"/>
    <rect class="icon" x="340" y="51" width="2" height="2"/>
    <text class="contact" x="343.5" y="53.2">info@marigoldloft.com.hk</text>
    <circle class="icon" cx="341" cy="57.5" r="1"/>
    <text class="contact" x="343.5" y="58.7">www.marigoldloft.com.hk</text>
  </g>

  <!-- ===== Document envelope ===== -->
  <g class="document-envelope">
    <rect class="paper" x="423" y="36" width="219" height="283"/>
    <path class="ink" d="M423,36 L642,36 L631,69 L432,69 Z"/>
    <line x1="430" y1="72" x2="425" y2="316" stroke="#ddd" stroke-width="0.4"/>
    <line x1="635" y1="72" x2="640" y2="316" stroke="#ddd" stroke-width="0.4"/>
    <rect class="brand-square" x="523" y="48" width="9" height="9" stroke-width="0.9"/>
  </g>

  <!-- ===== Letterhead, curved edition ===== -->
  <g class="letterhead-curved">
    <rect class="paper" x="661" y="40" width="219" height="283"/>
    <path class="red" d="M693,40 C704,160 740,260 789,323 L771,323 C730,255 700,160 690,40 Z"/>
    <path class="ink" d="M661,40 L690,40 C700,160 730,255 771,323 L661,323 Z"/>
    <g transform="translate(698,275) rotate(-90)">
      <rect class="brand-square" x="-13" y="-9" width="9" height="9" stroke-width="0.9"/>
      <text class="brand-name" x="0" y="-1" font-size="10">Marigold Image Loft</text>
    </g>
    <g transform="translate(868,112) rotate(-90)">
      <text font-family="Roboto, sans-serif" font-weight="700" font-size="5.4" fill="#111">www.marigoldloft.com.hk</text>
    </g>
    <circle class="icon" cx="866" cy="116" r="1.8"/>
  </g>

  <!-- ===== Envelope front ===== -->
  <g class="envelope-front">
    <rect class="paper" x="911" y="39" width="244" height="107"/>
    <path class="red" d="M911,106 C980,70 1070,48 1155,58 L1155,67 C1090,54 1000,72 911,114 Z"/>
    <path class="ink" d="M911,39 L1155,39 L1155,58 C1070,48 980,70 911,106 Z"/>
    <rect class="brand-square" x="922" y="55" width="8" height="8" stroke-width="0.9"/>
    <text class="brand-name" x="933" y="62.5" font-size="7">Marigold Image Loft</text>
    <circle class="icon" cx="1105" cy="135.5" r="1.1"/>
    <text class="contact dark" x="1108" y="136.6">www.marigoldloft.com.hk</text>
  </g>

  <!-- ===== Envelope back ===== -->
  <g class="envelope-back">
    <rect class="paper" x="911" y="151" width="244" height="107"/>
    <path class="ink" d="M911,151 L1155,151 L1146,188 L920,188 Z"/>
    <line x1="920" y1="190" x2="912" y2="256" stroke="#ddd" stroke-width="0.4"/>
    <line x1="1146" y1="190" x2="1154" y2="256" stroke="#ddd" stroke-width="0.4"/>
    <rect class="brand-square" x="1028" y="163" width="9" height="9" stroke-width="0.9"/>
    <text class="contact" x="1033" y="183.5" text-anchor="middle">Unit 4, 6/F, Harbourline Centre, 28 Fenwick Lane, Kestrel Bay</text>
  </g>

  <!-- ===== Paper folder ===== -->
  <g class="paper-folder">
    <rect fill="url(#glow)" x="66" y="341" width="437" height="383"/>
    <rect class="frame-line" x="70.5" y="345.5" width="209" height="273"/>
    <rect class="frame-line" x="290" y="345.5" width="209" height="273"/>
    <path fill="#4a4a4a" d="M264,624 L284,624 L306,724 L285,724 Z"/>

    <!-- back panel -->
    <rect class="brand-square" x="146" y="535" width="11" height="11" stroke-width="1"/>
    <text class="brand-name" x="160" y="546" font-size="8.6">Marigold Image Loft</text>
    <text class="contact" x="120" y="576">Unit 4, 6/F, Harbourline</text>
    <text class="contact" x="120" y="580">Centre, 28 Fenwick Lane,</text>
    <text class="contact" x="120" y="584">Kestrel Bay</text>
    <line x1="158" y1="572" x2="158" y2="585" stroke="#555" stroke-width="0.3"/>
    <rect class="icon" x="162" y="574" width="2" height="2"/>
    <text class="contact" x="165.5" y="576.3">(852) 2310 4478</text>
    <rect class="icon" x="162" y="580.5" width="2" height="2"/>
    <text class="contact" x="165.5" y="582.8">(852) 2310 4479</text>
    <rect class="icon" x="203" y="574" width="2" height="2"/>
    <text class="contact" x="206.5" y="576.3">info@marigoldloft.com.hk</text>
    <circle class="icon" cx="204" cy="581.5" r="1"/>
    <text class="contact" x="206.5" y="582.8">www.marigoldloft.com.hk</text>

    <!-- front panel -->
    <rect class="brand-square" x="332" y="416" width="20" height="20" stroke-width="1.4"/>
    <text class="brand-name" x="358" y="434" font-size="12.5">Marigold Image Loft</text>
    <circle class="icon" cx="377" cy="607.5" r="1.1"/>
    <text class="contact" x="380" y="608.6">www.marigoldloft.com.hk</text>

    <!-- left pocket, set upside down -->
    <g transform="rotate(180 164 670)">
      <rect class="brand-square" x="128" y="662" width="11" height="11" stroke-width="1"/>
      <text class="brand-name" x="142" y="673" font-size="8.6">Marigold Image Loft</text>
    </g>

    <!-- right pocket business card, set upside down -->
    <g transform="rotate(180 404 672)">
      <rect class="frame-line" x="346" y="641" width="117" height="63"/>
      <rect class="brand-square" x="356" y="652" width="8" height="8" stroke-width="0.9"/>
      <text class="brand-name" x="367" y="659.5" font-size="6.6">Marigold Image Loft</text>
      <text class="holder-name" x="357" y="676">OWEN <tspan class="surname">PRYCE</tspan><tspan class="contact" dx="1.5"> |  Photographer</tspan></text>
      <text class="contact" x="357" y="682">Unit 4, 6/F, Harbourline</text>
      <text class="contact" x="357" y="685.5">Centre, 28 Fenwick Lane,</text>
      <text class="contact" x="357" y="689">Kestrel Bay</text>
      <text class="contact" x="390" y="682">(852) 2310 4478</text>
      <text class="contact" x="390" y="686.5">(852) 9120 3386</text>
      <text class="contact" x="416" y="682">(852) 2310 4479</text>
      <text class="contact" x="416" y="686.5">info@marigoldloft.com.hk</text>
    </g>
  </g>

  <!-- ===== CD sleeve ===== -->
  <g class="cd-sleeve">
    <rect fill="url(#glow)" x="552" y="344" width="226" height="226"/>
    <path class="red" d="M552,344 L778,344 L778,424 C740,385 680,360 620,358 C590,357 565,362 552,368 Z"/>
    <path fill="#1a1a1a" d="M552,368 C565,362 590,357 620,358 C680,360 740,385 778,424 L778,432 C740,395 680,368 620,366 C590,365 565,370 552,376 Z"/>
    <rect class="brand-square" x="568" y="395" width="24" height="24" stroke-width="1.5"/>
    <text class="brand-name" x="600" y="414" font-size="12.5">Marigold Image Loft</text>
    <text class="brand-cn" x="614" y="446" font-size="10">金盞影像工作室</text>
    <rect class="icon" x="580" y="554.5" width="2.4" height="2.4"/>
    <text class="contact" x="584.5" y="557.3">(852) 2310 4478</text>
    <rect class="icon" x="636" y="554.5" width="2.4" height="2.4"/>
    <text class="contact" x="640.5" y="557.3">info@marigoldloft.com.hk</text>
    <circle class="icon" cx="705" cy="555.7" r="1.2"/>
    <text class="contact" x="708" y="557.3">www.marigoldloft.com.hk</text>
  </g>

  <!-- ===== CD disc ===== -->
  <g class="cd-disc">
    <circle class="ink" cx="890" cy="622" r="113"/>
    <path class="paper" d="M890,622 L777,622 A113,113 0 0 0 978,693 Z"/>
    <circle class="frame-line" cx="890" cy="622" r="98"/>
    <text class="cd-ring-text"><textPath href="#cd-ring" startOffset="0">Copyright  Copyright  Copyright  Copyright  Copyright  Copyright  Copyright  Copyright  Copyright  Copyright  Copyright  Copyright  Copyright  Copyright  Copyright  Copyright  Copyright  Copyright  Copyright  Copyright  Copyright  Copyright  Copyright  Copyright  Copyright  Copyright  Copyright  Copyright</textPath></text>
    <circle fill="#4a4a4a" cx="890" cy="622" r="28"/>
    <circle fill="none" stroke="#333" stroke-width="3" cx="890" cy="622" r="29.5"/>
    <circle fill="none" stroke="var(--brand-red)" stroke-width="0.7" cx="890" cy="622" r="27"/>
    <rect class="brand-square" x="842" y="559" width="15" height="15" stroke-width="1.1"/>
    <text class="brand-name" x="862" y="571" font-size="9.5">Marigold Image Loft</text>
    <text class="brand-cn" x="800" y="614" font-size="6.5">金盞影像工作室</text>
    <text class="cd-label client" x="828" y="645" font-size="4.4">Client Name</text>
    <text class="cd-label" x="828" y="652" font-size="3.4">Age</text>
    <text class="cd-label" x="828" y="658.5" font-size="3.4">Date</text>
    <rect class="icon" x="873" y="678" width="2.2" height="2.2"/>
    <text class="contact dark" x="877" y="680.3">(852) 2310 4478</text>
    <rect class="icon" x="869" y="686" width="2.2" height="2.2"/>
    <text class="contact dark" x="873" y="688.3">info@marigoldloft.com.hk</text>
    <circle class="icon" cx="871" cy="695.2" r="1.1"/>
    <text class="contact dark" x="873.5" y="696.5">www.marigoldloft.com.hk</text>
  </g>
</svg>
</body>
</html>
```